Professional looking Roller Blind Discount Card that portrays quality at a value for money price!

We need a double sided business card designed as a discount card. Size 90mm wide x 55mm high.We would like it to look professional and portray quality at a value for money price point.I have uploaded a word document with a basic layout with the information we want included on each side of the card. Please put your own thought into the layout.

Contact Information for Business Card

As per word document attached.

```html
<!DOCTYPE html>
<html lang="en">
<head>
<meta charset="UTF-8">
<title>Roller Blinds Discount Card</title>
<link rel="stylesheet" href="https://fonts.googleapis.com/css2?family=Arimo:wght@700&family=Caladea:wght@400;700&family=Noto+Sans:wght@400&family=Roboto+Slab:wght@400;600;700&display=swap">
<style>
  :root {
    --teal-deep: #1b4f58;
    --teal-head: #137178;
    --teal-light: #4fa8b0;
    --ribbon-light: #f4f5f6;
    --ribbon-shade: #d4d7d9;
    --ribbon-fold: #8a8d90;
    --gold-light: #f6d98a;
    --gold-dark: #b9862a;
    --paper: #ffffff;
    --brand-blue: #2a9fe0;
  }
  * { margin: 0; padding: 0; box-sizing: border-box; }
  html, body { width: 1200px; height: 1200px; overflow: hidden; background: var(--paper); }
  .canvas { position: relative; width: 1200px; height: 1200px; }

  .card {
    position: absolute;
    left: 266px;
    width: 676px;
    height: 413px;
    overflow: hidden;
  }
  .card--front { top: 150px; background: var(--paper); border: 1px solid var(--teal-deep); }
  .card--back { top: 645px; background: var(--teal-deep); }

  /* Front */
  .offer {
    position: absolute; top: 14px; left: 0; width: 100%;
    display: flex; justify-content: center; align-items: center; gap: 18px;
  }
  .offer__rule { width: 72px; height: 12px; }
  .offer__headline {
    font-family: "Arimo", sans-serif; font-weight: 700;
    font-size: 104px; line-height: 1; color: var(--teal-head); letter-spacing: 1px;
  }
  .offer__headline .pct { font-size: 44px; margin: 0 12px 0 2px; }
  .offer__sub {
    position: absolute; top: 110px; width: 100%; text-align: center;
    font-family: "Caladea", serif; font-size: 33px; color: var(--teal-light);
  }
  .band { position: absolute; top: 186px; left: 0; width: 100%; height: 155px; background: var(--teal-deep); }
  .ribbon { position: absolute; top: 158px; left: 112px; width: 452px; height: 38px; }
  .ribbon__text {
    position: absolute; top: 161px; left: 112px; width: 452px; text-align: center;
    font-family: "Caladea", serif; font-weight: 700; font-size: 22px; color: var(--teal-head);
  }
  .ribbon__text .sep { color: var(--teal-light); font-weight: 400; margin: 0 8px; }
  .seal { position: absolute; top: 198px; width: 140px; height: 130px; }
  .seal--1 { left: 74px; } .seal--2 { left: 268px; } .seal--3 { left: 462px; }
  .call {
    position: absolute; width: 100%; text-align: center; white-space: nowrap;
  }
  .card--front .call {
    top: 346px; color: var(--teal-head);
    font-family: "Roboto Slab", serif; font-size: 30px;
  }
  .card--front .call .num { font-family: "Noto Sans", sans-serif; font-size: 37px; margin: 0 6px; }

  /* Back */
  .title {
    position: absolute; top: 22px; width: 100%; text-align: center;
    font-family: "Roboto Slab", serif; font-weight: 600; font-size: 92px;
    color: var(--teal-light); line-height: 1;
  }
  .strip {
    position: absolute; top: 125px; left: 0; width: 100%; height: 36px;
    background: var(--teal-light); text-align: center;
    font-family: "Caladea", serif; font-size: 29px; line-height: 36px; color: var(--paper);
  }
  .strip b { font-weight: 700; }
  .gallery { position: absolute; top: 180px; left: 44px; width: 590px; height: 150px; }
  .card--back .call {
    top: 346px; left: 28px; width: auto; text-align: left;
    font-family: "Roboto Slab", serif; font-size: 33px; color: var(--teal-light);
  }
  .card--back .call .num { font-weight: 700; font-size: 40px; margin: 0 8px; letter-spacing: 1px; }
  .brand {
    position: absolute; top: 360px; left: 492px;
    display: flex; align-items: center; gap: 8px;
    font-family: "Caladea", serif; font-size: 20px; color: var(--brand-blue); white-space: nowrap;
  }
  .brand__mark { width: 12px; height: 12px; background: var(--brand-blue); }
</style>
</head>
<body>
<div class="canvas">

  <section class="card card--front">
    <div class="offer">
      <svg class="offer__rule" viewBox="0 0 72 12"><polygon points="0,6 72,0 72,12" fill="var(--teal-head)"/></svg>
      <div class="offer__headline">25<span class="pct">%</span>Off</div>
      <svg class="offer__rule" viewBox="0 0 72 12"><polygon points="0,0 72,6 0,12" fill="var(--teal-head)"/></svg>
    </div>
    <p class="offer__sub">Quality Custom Made Roller Blinds</p>

    <div class="band"></div>
    <svg class="ribbon" viewBox="0 0 452 38" preserveAspectRatio="none">
      <defs>
        <linearGradient id="ribbonFill" x1="0" y1="0" x2="0" y2="1">
          <stop offset="0" stop-color="var(--ribbon-light)"/>
          <stop offset="1" stop-color="var(--ribbon-shade)"/>
        </linearGradient>
      </defs>
      <polygon points="0,28 11,0 11,28" fill="var(--ribbon-fold)"/>
      <polygon points="452,28 441,0 441,28" fill="var(--ribbon-fold)"/>
      <rect x="11" y="0" width="430" height="36" rx="5" fill="url(#ribbonFill)"/>
    </svg>
    <div class="ribbon__text">Block out<span class="sep">|</span>Screen<span class="sep">|</span>Light Filtering</div>

    <svg class="seal seal--1" viewBox="0 0 140 130" role="img" aria-label="Gold seal: best price guarantee">
      <defs>
        <radialGradient id="gold" cx="0.4" cy="0.35" r="0.7">
          <stop offset="0" stop-color="var(--gold-light)"/>
          <stop offset="1" stop-color="var(--gold-dark)"/>
        </radialGradient>
      </defs>
      <circle cx="70" cy="65" r="63" fill="url(#gold)"/>
    </svg>
    <svg class="seal seal--2" viewBox="0 0 140 130" role="img" aria-label="Gold seal: free in-home measure and quote">
      <circle cx="70" cy="65" r="63" fill="url(#gold)"/>
    </svg>
    <svg class="seal seal--3" viewBox="0 0 140 130" role="img" aria-label="Gold seal: family owned and operated">
      <circle cx="70" cy="65" r="63" fill="url(#gold)"/>
    </svg>

    <p class="call">Call<span class="num">0491 570 159</span>Today!</p>
  </section>

  <section class="card card--back">
    <h1 class="title">Roller Blinds</h1>
    <div class="strip"><b>FREE</b> in Home Meacsure &amp; Quotes</div>

    <svg class="gallery" viewBox="0 0 590 150">
      <defs>
        <linearGradient id="photoGrey" x1="0" y1="0" x2="1" y2="1">
          <stop offset="0" stop-color="#e6e7e8"/>
          <stop offset="1" stop-color="#7d8084"/>
        </linearGradient>
        <linearGradient id="photoBeige" x1="0" y1="0" x2="0" y2="1">
          <stop offset="0" stop-color="#d9cfc4"/>
          <stop offset="1" stop-color="#b9a99a"/>
        </linearGradient>
        <linearGradient id="photoSwatch" x1="0" y1="0" x2="1" y2="0">
          <stop offset="0" stop-color="#8a7f6d"/>
          <stop offset="0.5" stop-color="#e2e0da"/>
          <stop offset="1" stop-color="#a9bfd6"/>
        </linearGradient>
      </defs>
      <g role="img" aria-label="Photo of a grey roller blind mounted below a ceiling">
        <path d="M20,70 C0,40 40,20 70,30 C90,5 140,5 160,20 C190,0 240,5 250,30 C280,20 300,45 285,70 C300,95 270,120 245,110 C230,140 180,145 160,125 C130,148 80,145 70,120 C35,130 5,100 20,70 Z" fill="url(#photoGrey)" stroke="#fff" stroke-width="4"/>
      </g>
      <g role="img" aria-label="Photo of striped light-filtering blinds over a window">
        <path d="M250,60 C240,30 280,15 300,25 C320,5 360,5 380,20 C410,5 450,15 445,45 C460,65 445,90 425,90 C420,115 380,120 365,105 C340,125 300,120 295,100 C265,105 240,85 250,60 Z" fill="url(#photoBeige)" stroke="#fff" stroke-width="4"/>
      </g>
      <g role="img" aria-label="Photo of roller blind fabric samples in neutral and blue tones">
        <path d="M445,40 C440,15 470,0 490,8 C510,-5 545,0 555,15 C580,10 595,35 580,50 C595,65 575,90 555,82 C545,105 505,105 495,90 C470,100 440,85 450,65 C430,58 435,42 445,40 Z" fill="url(#photoSwatch)" stroke="#fff" stroke-width="4"/>
      </g>
    </svg>

    <p class="call">Call<span class="num">0491 570 159</span>Today!</p>
    <div class="brand"><span class="brand__mark"></span>K&amp;L INTERIORS</div>
  </section>

</div>
</body>
</html>
```